Business Card for Bloom Vitality & Strength

Hi can you please design a business card with my logo and program logo (the new one I just sent) somewhere on it too maybe on the back? Needs to be eye catching and super cool.
Trudy Melcombe, Director
Master Personal Trainer & Nutrition Coach
0472 816 305
Www.bloomvitalitystrength.com.au
Insta (logo) bloom_vitality_strength #bloomyou7x72018

Target Market(s)

30+ women looking to change lifestyle to healthy mind body etc

Industry/Entity Type

Health And Wellness

Contact Information for Business Card

As above

Font styles to use
Sans Serif

Colors

Designer to choose colors to be used in the design.

Requirements
Must have
• Must super cool and edgy with a bit of cuteness

```html
<!DOCTYPE html>
<html lang="en">
<head>
<meta charset="utf-8">
<title>Bloom Vitality &amp; Strength — Business Card</title>
<link href="https://fonts.googleapis.com/css2?family=Montserrat:wght@400;500;700&display=swap" rel="stylesheet">
<style>
  :root {
    --backdrop: #e4e4e6;
    --card: #ffffff;
    --ink: #111111;
    --ink-soft: #333333;
    --rule: #555555;
    --accent: #d9161c;
    --shadow: rgba(0,0,0,0.18);
  }
  * { box-sizing: border-box; margin: 0; padding: 0; }
  html, body { width: 1200px; height: 880px; overflow: hidden; }
  body {
    background: var(--backdrop);
    font-family: "Montserrat", Arial, sans-serif;
    color: var(--ink);
    position: relative;
  }
  .card {
    position: absolute;
    width: 560px;
    height: 320px;
    background: var(--card);
    border-radius: 22px;
    box-shadow: 0 10px 30px var(--shadow);
    overflow: hidden;
  }
  .card--front { left: 30px; top: 280px; }
  .card--back { left: 610px; top: 280px; }

  .program {
    position: absolute;
    width: 300px;
    text-align: center;
  }
  .card--front .program { left: 130px; top: 108px; }
  .card--back .program { right: 34px; top: 36px; width: 270px; }

  .program__rule { height: 1.5px; background: var(--rule); }
  .program__rule--top { margin: 0 0 12px 40px; }
  .program__rule--bottom { margin: 12px 40px 0 0; }

  .program-mark {
    display: inline-flex;
    align-items: center;
    gap: 10px;
    font-weight: 500;
    color: var(--ink);
    letter-spacing: 1px;
    white-space: nowrap;
  }
  .program-mark__dot { border-radius: 50%; background: var(--accent); flex: none; }
  .card--front .program-mark { font-size: 30px; }
  .card--front .program-mark__dot { width: 24px; height: 24px; }
  .card--back .program-mark { font-size: 26px; }
  .card--back .program-mark__dot { width: 20px; height: 20px; }

  .program-tag {
    margin-top: 6px;
    font-size: 10px;
    font-weight: 500;
    letter-spacing: 1.5px;
    text-transform: uppercase;
    color: var(--ink-soft);
  }
  .program-by {
    margin-top: 3px;
    font-size: 10px;
    color: var(--ink-soft);
  }

  .social {
    position: absolute;
    right: 30px;
    top: 178px;
    display: flex;
    gap: 10px;
  }
  .social__dot { width: 22px; height: 22px; border-radius: 50%; background: var(--accent); }

  .person { position: absolute; left: 40px; top: 160px; }
  .person__name { font-size: 19px; font-weight: 700; letter-spacing: -0.3px; }
  .person__role { font-size: 14px; color: var(--accent); margin-top: 1px; }
  .person__title { font-size: 13px; color: var(--ink-soft); margin-top: 1px; }

  .divider {
    position: absolute;
    left: 40px;
    right: 24px;
    top: 224px;
    height: 1.5px;
    background: var(--accent);
  }

  .contact { position: absolute; left: 40px; top: 240px; list-style: none; }
  .contact__item { display: flex; align-items: center; gap: 10px; font-size: 13.5px; color: var(--ink-soft); height: 24px; }
  .contact__icon { width: 18px; height: 18px; flex: none; }
</style>
</head>
<body>

<section class="card card--front" aria-label="Card front">
  <div class="program">
    <div class="program__rule program__rule--top"></div>
    <div class="program-mark"><span class="program-mark__dot"></span>Renew Circle</div>
    <div class="program-tag">Strength Program</div>
    <div class="program-by">by Bloom Vitality &amp; Strength</div>
    <div class="program__rule program__rule--bottom"></div>
  </div>
</section>

<section class="card card--back" aria-label="Card back">
  <div class="program">
    <div class="program__rule program__rule--top"></div>
    <div class="program-mark"><span class="program-mark__dot"></span>Renew Circle</div>
    <div class="program-tag">Strength Program</div>
    <div class="program-by">by Bloom Vitality &amp; Strength</div>
    <div class="program__rule program__rule--bottom"></div>
  </div>

  <div class="social" aria-label="Social links">
    <span class="social__dot"></span>
    <span class="social__dot"></span>
  </div>

  <div class="person">
    <div class="person__name">Trudy Melcombe</div>
    <div class="person__role">Director</div>
    <div class="person__title">Master Personal Trainer &amp; Nutrition Coach</div>
  </div>

  <div class="divider"></div>

  <ul class="contact">
    <li class="contact__item">
      <svg class="contact__icon" viewBox="0 0 18 18" aria-hidden="true">
        <circle cx="9" cy="9" r="8" fill="none" stroke="#d9161c" stroke-width="1.3"/>
        <rect x="6.2" y="4.5" width="5.6" height="9" rx="1" fill="none" stroke="#d9161c" stroke-width="1.2"/>
        <line x1="8" y1="12" x2="10" y2="12" stroke="#d9161c" stroke-width="1"/>
      </svg>
      0472 816 305
    </li>
    <li class="contact__item">
      <svg class="contact__icon" viewBox="0 0 18 18" aria-hidden="true">
        <circle cx="9" cy="9" r="8" fill="none" stroke="#d9161c" stroke-width="1.3"/>
        <circle cx="9" cy="9" r="4.6" fill="none" stroke="#d9161c" stroke-width="1"/>
        <ellipse cx="9" cy="9" rx="2" ry="4.6" fill="none" stroke="#d9161c" stroke-width="1"/>
        <line x1="4.4" y1="9" x2="13.6" y2="9" stroke="#d9161c" stroke-width="1"/>
      </svg>
      www.bloomvitalitystrength.com.au
    </li>
  </ul>
</section>

</body>
</html>
```